TALL WAVE

I am in this industry for last 15 years we have done lots of commercial site like we work with ORBEL costruction, loam properties, DRV, quill construction.
We do all domestic and commercial wall and floor tiling, swimming pools, spas, paving, marbles blue stones and muchmore.

Specializing in the wall and floor Tiling, Waterproofing and floor preparations

Industry/Entity Type

Industry

Number of Pages Required

1 page

Font styles to use
Serif
Decorative

Colors

Designer to choose colors to be used in the design.

Requirements
Must have
• domestic and commercial indoor tiling, bathroom tiling and paving pictures
Nice to have
• beautiful bathroom pictures with tile

```html
<!DOCTYPE html>
<html lang="en">
<head>
<meta charset="utf-8">
<title>TALL WAVE – Tiling &amp; Construction</title>
<link rel="stylesheet" href="https://fonts.googleapis.com/css2?family=Damion&family=Crimson+Text:wght@400;600&family=Yanone+Kaffeesatz:wght@300;400&display=swap">
<style>
  :root {
    --purple: #8e72c4;
    --purple-deep: #6a3c9c;
    --red: #d5343c;
    --coral: #e8575a;
    --ink: #2b2b2b;
    --text: #3a3a3a;
    --rule: #d6d6d6;
    --white: #ffffff;
  }
  * { box-sizing: border-box; margin: 0; padding: 0; }
  html, body { width: 1200px; height: 1190px; overflow: hidden; background: var(--white); }
  body { position: relative; font-family: "Crimson Text", Georgia, serif; color: var(--text); }

  .hero {
    position: absolute; left: 0; top: 0; width: 1200px; height: 510px;
    background: linear-gradient(90deg, #6a3aa0 0%, #9a3c8c 40%, #c83a5a 75%, #d63b3f 100%);
  }
  .hero__photo {
    position: absolute; inset: 0;
    background: linear-gradient(180deg, rgba(40,10,40,0.25) 0%, rgba(255,255,255,0.05) 45%, rgba(60,10,40,0.2) 100%);
  }
  .hero__title {
    position: absolute; left: 0; width: 1200px; top: 40px; text-align: center;
    font-family: "Damion", cursive; font-weight: 400; font-size: 70px; color: var(--white); line-height: 1;
  }
  .hero__lead {
    position: absolute; left: 80px; width: 1040px; top: 154px; text-align: center;
    font-size: 17.5px; line-height: 30px; color: var(--white); font-weight: 600;
  }
  .btn-outline {
    position: absolute; display: flex; align-items: center; justify-content: center;
    border: 2px solid var(--white); border-radius: 40px; color: var(--white);
    font-weight: 600; text-decoration: none;
  }
  .hero__cta { left: 448px; top: 245px; width: 225px; height: 57px; font-size: 16px; }
  .hero__wave { position: absolute; left: 0; top: 420px; width: 1200px; height: 95px; }
  .scroll-down { position: absolute; left: 535px; top: 446px; width: 50px; height: 50px; }

  .services-head {
    position: absolute; left: 0; width: 1200px; top: 544px; text-align: center;
    font-family: "Yanone Kaffeesatz", sans-serif; font-weight: 300; font-size: 42px; color: var(--ink); line-height: 1;
  }
  .services-head .accent { color: var(--coral); font-weight: 400; }
  .services-head__icon {
    display: inline-block; width: 30px; height: 32px; vertical-align: -2px; margin-right: 4px;
    background: linear-gradient(180deg, #c9c9c9, #8a8a8a); border-radius: 4px;
  }
  .services-intro {
    position: absolute; left: 160px; width: 880px; top: 596px; text-align: center;
    font-size: 14px; line-height: 20px; color: var(--text);
  }

  .service-list { position: absolute; left: 55px; top: 687px; width: 130px; list-style: none; }
  .service-list li { position: relative; height: 132px; border-bottom: 2px solid var(--rule); margin-bottom: 4px; }
  .service-list li.is-active { border-bottom-color: var(--purple); }
  .service-list li:last-child { border-bottom-width: 2px; }
  .service-list .icon { position: absolute; left: 2px; top: 0; width: 58px; height: 50px; }
  .service-list .label {
    position: absolute; left: 0; bottom: 10px; font-family: "Damion", cursive; font-size: 19px; color: var(--ink); white-space: nowrap;
  }

  .service-panel { position: absolute; left: 260px; top: 687px; width: 803px; height: 503px; background: var(--purple); }
  .service-panel__pointer { position: absolute; left: -31px; top: 222px; width: 31px; height: 52px; }
  .gallery { position: absolute; left: 62px; top: 29px; width: 676px; }
  .gallery .shot { position: absolute; width: 159px; height: 114px; }
  .service-panel__text {
    position: absolute; left: 66px; top: 320px; width: 680px;
    font-size: 14.5px; line-height: 23.5px; color: var(--white);
  }
  .service-panel__cta { left: 71px; top: 434px; width: 133px; height: 35px; font-size: 14px; font-weight: 400; }
</style>
</head>
<body>

<header class="hero">
  <div class="hero__photo" role="img" aria-label="Photo of a wide paved plaza with trees and buildings, tinted purple to red"></div>
  <h1 class="hero__title">We are the builders of your dream world</h1>
  <p class="hero__lead">We are expert contruction engineers serving our customers for last 15 years. We work with passion, creativity and inovation and have done lots of commercial sites. We work with ORBEL costruction, loam properties, DRV, quill construction.</p>
  <a class="btn-outline hero__cta" href="#">Request a quote</a>
  <svg class="hero__wave" viewBox="0 0 1200 95" preserveAspectRatio="none" aria-hidden="true">
    <path d="M0,32 C180,8 360,6 560,40 C760,78 980,88 1200,60 L1200,95 L0,95 Z" fill="#ffffff"/>
  </svg>
  <svg class="scroll-down" viewBox="0 0 50 50" aria-hidden="true">
    <circle cx="25" cy="25" r="25" fill="#8e72c4"/>
    <path d="M13,20 L25,31 L37,20" fill="none" stroke="#ffffff" stroke-width="2"/>
  </svg>
</header>

<h2 class="services-head"><span class="services-head__icon" role="img" aria-label="Small worker illustration"></span>OUR <span class="accent">SERVICES</span></h2>
<p class="services-intro">Lorem ipsum dolor sit amet, consectetur adipiscing elit. Sed at lacus sed turpis cursus convallis id non tortor. Aenean condimentum tristique ex in tincidunt. Pellentesque vel purus convallis, vulputate ante ac, pellentesque est.</p>

<ul class="service-list">
  <li>
    <div class="icon" role="img" aria-label="Brick wall tiling illustration" style="background:linear-gradient(180deg,#d4c27a 0 30%,#b9302c 30% 100%)"></div>
    <span class="label">Wall Tiling</span>
  </li>
  <li class="is-active">
    <div class="icon" role="img" aria-label="Parquet floor tiling illustration" style="background:linear-gradient(135deg,#a0582a,#d89a5a,#a0582a)"></div>
    <span class="label">Floor Tiling</span>
  </li>
  <li>
    <div class="icon" role="img" aria-label="Waterproofing spray illustration" style="background:linear-gradient(90deg,#d8c23a 0 50%,#8a70c0 50% 100%)"></div>
    <span class="label">WaterProofing</span>
  </li>
  <li>
    <div class="icon" role="img" aria-label="Trowel and bricks floor preparation illustration" style="background:linear-gradient(90deg,#c8302e 0 60%,#d9a060 60% 100%)"></div>
    <span class="label">Floor preparations</span>
  </li>
</ul>

<section class="service-panel">
  <svg class="service-panel__pointer" viewBox="0 0 31 52" aria-hidden="true"><path d="M31,0 L0,26 L31,52 Z" fill="#8e72c4"/></svg>
  <div class="gallery">
    <div class="shot" style="left:0;top:0;background:linear-gradient(180deg,#9cc3dc,#d8d2c4 50%,#9a6a5a)" role="img" aria-label="Paved brick waterfront with city skyline"></div>
    <div class="shot" style="left:171px;top:0;background:linear-gradient(180deg,#e8e2d6,#b58a58 80%)" role="img" aria-label="Home hallway with wooden floor"></div>
    <div class="shot" style="left:343px;top:0;background:linear-gradient(180deg,#b8d0dc,#eef3f5 70%)" role="img" aria-label="Bright glass corridor with polished tiles"></div>
    <div class="shot" style="left:516px;top:0;background:linear-gradient(135deg,#d8b8a0,#ece8e2 50%,#cfcac2)" role="img" aria-label="Hands laying a white floor tile"></div>
    <div class="shot" style="left:2px;top:152px;background:linear-gradient(180deg,#b8642e,#e09a4a 60%,#c9803a)" role="img" aria-label="Tiled orange passage with lights"></div>
    <div class="shot" style="left:173px;top:152px;background:linear-gradient(180deg,#8a8a8a,#5a5a5a 60%,#2e2e2e)" role="img" aria-label="Paving stones being laid with a shovel"></div>
    <div class="shot" style="left:346px;top:152px;background:linear-gradient(90deg,#c8ccd4,#e8e0d0 50%,#c8c0b0)" role="img" aria-label="Worker on ladder preparing a wall"></div>
    <div class="shot" style="left:520px;top:152px;background:linear-gradient(180deg,#a8c4e0,#e8eef5 60%,#c8d4e4)" role="img" aria-label="Large hall with glossy tiled floor"></div>
  </div>
  <p class="service-panel__text">Lorem ipsum dolor sit amet, consectetur adipiscing elit. Sed at lacus sed turpis cursus convallis id non tortor. Aenean condimentum tristique ex in tincidunt. Pellentesque vel purus convallis, vulputate ante ac, pellentesque est. Phasellus sed lectus neque. Aenean mauris nulla, interdum vel eros vel, rutrum imperdiet elit. In consequat tempor sollicitudin.Maecenas efficitur viverra purus, eget tristique purus condimentum ac.</p>
  <a class="btn-outline service-panel__cta" href="#">Request a quote</a>
</section>

</body>
</html>
```